Oil and Gas Company: Letterhead Design

In short we need a professional company letterhead designed for our Oil and Gas company.

We would like to keep the design simple and professional. Letterhead to include the company logo and color scheme, front page and continuation pages.

For reference, see attached logo below with our company logo and color scheme.

Target Market(s)

Oil & Gas Market

Industry/Entity Type

Oil And Gas

Font styles to use
Sans Serif

Requirements
Must have
• Letterhead must contain a front page & continuation page.
• Must be simple and professional in design.
• Follow our logo and color scheme.
Nice to have
• I would like to have the logo embedded in the bottom right hand portion of the page to provide some depth into the letterhead.

```html
<!DOCTYPE html>
<html lang="en">
<head>
<meta charset="utf-8">
<title>Meridian Field Energy – Letterhead</title>
<link href="https://fonts.googleapis.com/css2?family=Open+Sans:wght@400;600&family=Lato:wght@400;700&display=swap" rel="stylesheet">
<style>
  :root {
    --brand-blue: #1257a6;
    --brand-red: #e2202a;
    --ink: #3f3f3f;
    --ink-dark: #222;
    --paper: #ffffff;
  }
  * { margin: 0; padding: 0; box-sizing: border-box; }
  html, body { width: 1040px; height: 1200px; overflow: hidden; background: var(--paper); }
  .letterhead {
    position: relative; width: 1040px; height: 1200px;
    font-family: "Open Sans", Arial, sans-serif; color: var(--ink);
  }
  .company-name {
    position: absolute; left: 600px; top: 200px; width: 380px;
    text-align: center; font-size: 28px; line-height: 31px;
    letter-spacing: 1.5px; color: var(--ink-dark); font-weight: 400;
  }
  .letter-meta, .recipient, .salutation, .letter-body, .closing, .signatory {
    position: absolute; left: 98px; font-size: 15.5px;
  }
  .letter-meta { top: 216px; }
  .recipient { top: 253px; line-height: 19px; font-style: normal; }
  .salutation { top: 356px; }
  .letter-body { top: 406px; width: 840px; line-height: 27px; text-align: justify; }
  .letter-body p { margin-bottom: 27px; }
  .closing { top: 815px; }
  .signatory { top: 890px; }
  .signatory-name { font-size: 19px; font-weight: 600; color: var(--ink-dark); }
  .signatory-title { font-size: 15.5px; margin-top: 6px; }
  .footer-bands { position: absolute; left: 0; top: 1073px; }
  .footer-contact, .footer-web {
    position: absolute; font-family: "Lato", Arial, sans-serif; color: #fff; font-size: 17px;
  }
  .footer-contact { left: 100px; top: 1103px; }
  .footer-contact .sep { margin: 0 8px; }
  .footer-web { right: 94px; top: 1085px; }
  .footer-address {
    position: absolute; left: 0; width: 1040px; top: 1153px; text-align: center;
    font-family: "Lato", Arial, sans-serif; font-size: 15px; color: var(--ink-dark);
  }
</style>
</head>
<body>
<main class="letterhead">
  <header class="company-name">MERIDIAN<br>FIELD ENERGY</header>

  <p class="letter-meta">Issuing Date: May 5, 2018</p>
  <address class="recipient">
    Name Of Employee Mr. XYZABC<br>Address of Employee<br>Address Line 2 etc..
  </address>

  <p class="salutation">Dear Mr.XYZABC</p>

  <section class="letter-body">
    <p>Lorem Ipsum has been the industry's standard dummy text ever since the 1500s, when an unknown printer took a galley of type and scrambled it to make a type specimen book. It has survived not only five centuries, but also the leap into electronic typesetting, remaining essentially unchanged. It was popularised in the 1960s with the release of Pressline sheets containing Lorem Ipsum passages, and more recently with desktop publishing software like Folio Layout including versions of Lorem Ipsum.</p>
    <p>Lorem Ipsum is simply dummy text of the printing and typesetting industry. Lorem Ipsum has been the industry's standard dummy text ever since the 1500s, when an unknown printer took a galley of type and scrambled it to make a type specimen book.</p>
    <p>It has survived not only five centuries, but also the leap into electronic typesetting, remaining essentially unchanged. It was popularised in the 1960s with the release of Pressline sheets containing Lorem IpsumIpsum passages.</p>
  </section>

  <p class="closing">Yours Sincerely</p>
  <div class="signatory">
    <p class="signatory-name">Daniel Hargrove</p>
    <p class="signatory-title">Managing Director</p>
  </div>

  <svg class="footer-bands" width="1040" height="65" viewBox="0 0 1040 65" aria-hidden="true">
    <polygon points="0,18 572,18 555,65 0,65" fill="var(--brand-blue)"/>
    <polygon points="582,0 1040,0 1040,65 560,65" fill="var(--brand-red)"/>
  </svg>
  <p class="footer-contact">P:&nbsp; 044-987 654 321<span class="sep">|</span>E: info@meridianfield.com</p>
  <p class="footer-web">www.meridianfield.com</p>
  <p class="footer-address">218, Harbour Road, Port District, 45210 Country Name</p>
</main>
</body>
</html>
```